Meridian Dash add on sales tool2017

This will be a flyer to leave with our clients we just did work for. We want to entice them to use our other services over the next 30 days with a discount, money off etc. we will write in the special and the expiration date. I want the client to read the description and see a picture of the service they may want done.

Target Market(s)

Repeat clients

Industry/Entity Type

Cleaning Service

Font styles to use
Serif
Sans Serif

Colors
ec1f27
000000
b1b1b1

Requirements
Must have
• Call to action! look high end market, clients show we do 1st class work.
• Don't Waite
Nice to have
• Classy, quality, I'm open to using other pictures that may look better
Should not have
• Look like a typical carpet cleaners special flyer
• Not to look cluttered

```html
<!DOCTYPE html>
<html lang="en">
<head>
<meta charset="utf-8">
<title>Meridian Dash – 30 Day Special Offer</title>
<link href="https://fonts.googleapis.com/css2?family=Bebas+Neue&family=Lato:wght@400;700;900&family=Roboto+Condensed:wght@700&display=swap" rel="stylesheet">
<style>
  :root{
    --red:#ec1f27;
    --black:#000000;
    --silver:#b1b1b1;
    --panel:#d1d2d4;
    --wave-light:#bdbec0;
    --wave-mid:#9c9d9f;
    --wave-dark:#808183;
    --ink:#1c1c1c;
    --white:#ffffff;
  }
  *{box-sizing:border-box;margin:0;padding:0}
  html,body{width:928px;height:1200px;overflow:hidden;background:var(--panel)}
  .flyer{position:relative;width:928px;height:1200px;background:var(--panel);overflow:hidden;font-family:'Lato',sans-serif;color:var(--ink)}
  .waves{position:absolute;left:0;top:0;width:928px;height:1200px}

  .masthead{position:absolute;left:0;top:0;width:928px;height:189px;background:var(--black)}
  .brand{position:absolute;left:49px;top:92px;display:flex;flex-direction:column;gap:6px}
  .brand-row{display:flex;align-items:center;gap:12px}
  .brand-mark{width:26px;height:26px;background:var(--red)}
  .brand-name{font-family:'Lato',sans-serif;font-weight:900;font-size:31px;letter-spacing:1px;color:var(--white);line-height:1}
  .brand-tagline{font-family:'Lato',sans-serif;font-weight:400;font-size:15px;letter-spacing:2px;color:var(--silver)}

  .offer{position:absolute;left:533px;top:26px;width:370px}
  .offer-title{font-family:'Bebas Neue',sans-serif;font-size:52px;line-height:1;color:var(--red);letter-spacing:.5px;white-space:nowrap}
  .offer-card{margin-top:4px;margin-left:3px;width:363px;height:106px;background:var(--white);border-radius:8px;overflow:hidden}
  .offer-card-label{height:31px;background:var(--red);color:var(--white);font-family:'Lato',sans-serif;font-weight:900;font-size:23px;text-align:center;line-height:31px}

  .headline{position:absolute;left:44px;top:208px;font-family:'Roboto Condensed',sans-serif;font-weight:700;font-size:45px;line-height:1.17;color:var(--ink)}

  .services{position:absolute;left:44px;top:0;width:468px}
  .service{position:absolute;left:0;width:468px}
  .service h2{font-family:'Lato',sans-serif;font-weight:700;font-size:22px;color:var(--red);letter-spacing:-.3px;line-height:1.15;margin-bottom:3px;white-space:nowrap}
  .service p{font-size:16.2px;line-height:22px;text-align:justify;letter-spacing:-.2px}
  .carpet{top:345px}
  .upholstery{top:459px}
  .drapery{top:572px}
  .tile{top:690px}
  .stone{top:803px}

  .gallery{position:absolute;left:542px;top:196px;width:360px;height:816px}

  .contact{position:absolute;left:27px;top:1050px}
  .address{font-family:'Roboto Condensed',sans-serif;font-weight:700;font-size:25px;color:var(--ink);white-space:nowrap}
  .phone-box{position:relative;margin-top:20px;width:405px;height:79px;border:3px solid var(--black);display:flex;align-items:center;justify-content:center}
  .phone-label{position:absolute;top:-13px;left:50%;transform:translateX(-50%);padding:0 6px;background:var(--wave-mid);font-family:'Roboto Condensed',sans-serif;font-weight:700;font-size:17px;color:var(--red);white-space:nowrap;line-height:22px}
  .phone-number{font-family:'Roboto Condensed',sans-serif;font-weight:700;font-size:66px;letter-spacing:1px;color:var(--black);line-height:1}
</style>
</head>
<body>
<div class="flyer">

  <svg class="waves" viewBox="0 0 928 1200" aria-hidden="true">
    <path d="M0,925 C180,860 400,875 560,960 C700,1035 820,1075 928,1075 L928,1200 L0,1200 Z" fill="#e3e4e5"/>
    <path d="M0,935 C190,875 410,890 570,975 C710,1050 830,1090 928,1090 L928,1200 L0,1200 Z" fill="var(--wave-light)"/>
    <path d="M0,1010 C200,960 420,980 600,1070 C720,1130 830,1150 928,1140 L928,1200 L0,1200 Z" fill="var(--wave-mid)"/>
    <path d="M480,1020 C610,1110 790,1150 928,1098 L928,1060 C800,1110 640,1095 480,1020 Z" fill="var(--red)"/>
    <path d="M520,1120 C660,1165 800,1165 928,1130 L928,1200 L560,1200 Z" fill="var(--wave-dark)"/>
    <path d="M540,1150 C680,1175 810,1170 928,1148" fill="none" stroke="#e9e9ea" stroke-width="3"/>
  </svg>

  <header class="masthead">
    <div class="brand">
      <div class="brand-row">
        <span class="brand-mark"></span>
        <span class="brand-name">MERIDIAN DASH</span>
      </div>
      <span class="brand-tagline">FINE CARE FOR EVERY SURFACE</span>
    </div>
    <div class="offer">
      <div class="offer-title">30 DAY SPECIAL OFFER!</div>
      <div class="offer-card">
        <div class="offer-card-label">EXPIRES</div>
      </div>
    </div>
  </header>

  <h1 class="headline">One Stop For All Your<br>Home Cleaning Needs</h1>

  <section class="services">
    <article class="service carpet">
      <h2>CARPET CLEANING</h2>
      <p>Don't let dirty carpets spoil the look of your beautiful home!. with 37 years of cleaning carpets experience you can expect your carpets to look like new in most cases.</p>
    </article>
    <article class="service upholstery">
      <h2>UPHOLSTERY CLEANING</h2>
      <p>Every day use leaves your sofa's and chairs looking dingy and can smell like dog. Our Dry cleaning ,Shampoo or Rinse extraction will leave the fabric feel like clean sheet!</p>
    </article>
    <article class="service drapery">
      <h2>DARAPERY CLEANING</h2>
      <p>Drapery's act like a filter attracting atmospheric soil! Making them look dingy, We make it easy to Dry clean in-home! Safe and effective beautiful drapery again.</p>
    </article>
    <article class="service tile">
      <h2>TILE &amp; GROUT CLEANING</h2>
      <p>Tile &amp; Grout get neglected! Dirty grout can leave permanent staining. Let our professionals bring back the look of a new floor.</p>
    </article>
    <article class="service stone">
      <h2>NATURAL STONE CLEANING &amp; POLISHING</h2>
      <p style="text-align:left">A dull stained Marble - Granite-Travertine and other Natural stone can be revitalized to look NEW again!</p>
    </article>
  </section>

  <svg class="gallery" viewBox="0 0 360 816">
    <defs>
      <linearGradient id="g-stairs" x1="0" y1="0" x2="1" y2="1"><stop offset="0" stop-color="#8a7a66"/><stop offset=".5" stop-color="#d9d5cf"/><stop offset="1" stop-color="#a9a39a"/></linearGradient>
      <linearGradient id="g-sofa" x1="0" y1="0" x2="1" y2="1"><stop offset="0" stop-color="#c9c3b4"/><stop offset=".6" stop-color="#8f8a76"/><stop offset="1" stop-color="#6e3f34"/></linearGradient>
      <linearGradient id="g-drape" x1="0" y1="0" x2="1" y2="0"><stop offset="0" stop-color="#7a5a4a"/><stop offset=".5" stop-color="#3a3030"/><stop offset="1" stop-color="#c7c3c0"/></linearGradient>
      <linearGradient id="g-tile" x1="0" y1="0" x2="1" y2="1"><stop offset="0" stop-color="#6f6c6a"/><stop offset=".5" stop-color="#a9a49c"/><stop offset="1" stop-color="#8c8a8a"/></linearGradient>
      <linearGradient id="g-stone" x1="0" y1="0" x2="0" y2="1"><stop offset="0" stop-color="#a8a29a"/><stop offset=".5" stop-color="#e6e3df"/><stop offset="1" stop-color="#8f8c88"/></linearGradient>
    </defs>
    <polygon role="img" aria-label="Photo: freshly cleaned carpeted staircase" points="0,0 360,0 360,150 0,176" fill="url(#g-stairs)"/>
    <polygon role="img" aria-label="Photo: sofa upholstery before and after cleaning" points="0,176 360,150 360,352 0,344" fill="url(#g-sofa)"/>
    <line x1="196" y1="162" x2="196" y2="348" stroke="#ffffff" stroke-width="3"/>
    <polygon role="img" aria-label="Photo: technician cleaning drapes in a home" points="0,344 360,352 360,486 0,496" fill="url(#g-drape)"/>
    <polygon role="img" aria-label="Photo: travertine tile floor with clean grout" points="0,496 360,486 360,660 0,664" fill="url(#g-tile)"/>
    <polygon role="img" aria-label="Photo: polished marble floor in a bright hallway" points="0,664 360,660 360,816 0,816" fill="url(#g-stone)"/>
    <g fill="none" stroke="#ffffff" stroke-width="2">
      <polyline points="0,176 360,150"/>
      <polyline points="0,344 360,352"/>
      <polyline points="0,496 360,486"/>
      <polyline points="0,664 360,660"/>
    </g>
  </svg>

  <footer class="contact">
    <div class="address">1450 W. Canyon Ridge Rd. Suite C, Las Vegas</div>
    <div class="phone-box">
      <span class="phone-label">Call Now To Book</span>
      <span class="phone-number">702 555-0147</span>
    </div>
  </footer>

</div>
</body>
</html>
```